Redesign of iOS App Moriva Tutor

Redesign of existing App Moriva Tutor, an app that helps learning Japanese Kanjis, Hiragana, Katakana.

The functionallity should remain the same as today: the app is free, you may download it at the app store. But: I like the design of my other apps better ;)

Target Market(s)

Students learning Japanese

Industry/Entity Type

Teacher

Font styles to use
Sans Serif

Requirements
Must have
• Moriva Tutor has 7 main screens, all screens has to be designed for iPhone and iPad: Main, Settings, Reading Tests, Writing Tests, Game, Paper Mode, Search
Nice to have
• I like the logo as it is today

```html
<!DOCTYPE html>
<html lang="en">
<head>
<meta charset="utf-8">
<title>Moriva Tutor – Reading Test</title>
<link rel="stylesheet" href="https://fonts.googleapis.com/css2?family=Nunito:wght@400;600;700&family=Noto+Sans+JP:wght@400;500&display=swap">
<style>
  :root {
    --bg: #ffffff;
    --ink: #111111;
    --lives: #e8574a;
    --score: #5b9bd5;
    --coins: #f5a623;
    --rule: #9a9a9a;
    --tile: #f2f2f4;
    --tile-border: #d4d4d8;
    --kanji-faded: #e0e0e2;
    --action: #f7e08a;
    --action-border: #e9cc62;
    --action-text: #3a3a48;
    --back-bg: #f2f2f4;
    --back-border: #d0d0d4;
  }
  * { box-sizing: border-box; margin: 0; padding: 0; }
  html, body { width: 675px; height: 1200px; overflow: hidden; background: var(--bg); }
  body { font-family: "Nunito", sans-serif; position: relative; color: var(--ink); }

  .status-bar { position: absolute; top: 0; left: 0; width: 675px; height: 36px; font-size: 17px; font-weight: 400; }
  .status-bar .signal { position: absolute; left: 11px; top: 11px; }
  .status-bar .time { position: absolute; left: 0; width: 675px; top: 7px; text-align: center; }
  .status-bar .battery-level { position: absolute; right: 72px; top: 7px; }
  .status-bar .battery { position: absolute; right: 11px; top: 10px; }

  .stats { position: absolute; top: 60px; left: 0; width: 675px; height: 80px; }
  .stat { position: absolute; width: 200px; text-align: center; line-height: 1; }
  .stat .label, .stat .sub { font-size: 20px; }
  .stat .value { font-size: 33px; margin: 1px 0 0; }
  .stat .sub { margin-top: 0; }
  .stat.lives { left: 26px; color: var(--lives); }
  .stat.score { left: 237px; color: var(--score); }
  .stat.coins { left: 447px; color: var(--coins); }

  .rule { position: absolute; left: 34px; width: 609px; height: 2px; background: var(--rule); }
  .rule.top { top: 148px; }
  .rule.bottom { top: 319px; }

  .prompt { position: absolute; top: 176px; left: 0; width: 675px; text-align: center;
    font-family: "Noto Sans JP", sans-serif; font-size: 58px; font-weight: 400; line-height: 1.1; }

  .choices { position: absolute; top: 356px; left: 34px; width: 606px;
    display: grid; grid-template-columns: repeat(3, 186px); grid-auto-rows: 186px; column-gap: 24px; row-gap: 29px; }
  .choice { background: var(--tile); border: 1.5px solid var(--tile-border); border-radius: 4px;
    display: flex; align-items: center; justify-content: center;
    font-family: "Noto Sans JP", sans-serif; font-size: 66px; color: var(--ink); }
  .choice.eliminated { color: var(--kanji-faded); }

  .back { position: absolute; left: 34px; top: 1079px; width: 60px; height: 60px; border-radius: 50%;
    background: var(--back-bg); border: 1.5px solid var(--back-border); display: flex; align-items: center; justify-content: center; }
  .action { position: absolute; top: 1052px; width: 113px; height: 113px; border-radius: 50%;
    background: var(--action); border: 1.5px solid var(--action-border);
    display: flex; flex-direction: column; align-items: center; justify-content: center;
    color: var(--action-text); font-weight: 700; font-size: 20px; line-height: 1.25; text-align: center; }
  .action .cost { font-size: 14px; font-weight: 700; line-height: 1.1; }
  .action.level-up { left: 146px; }
  .action.live-plus { left: 273px; }
  .action.split { left: 400px; }
  .action.hint { left: 527px; }
</style>
</head>
<body>
  <header class="status-bar">
    <svg class="signal" width="92" height="14" viewBox="0 0 92 14" aria-hidden="true">
      <g fill="#333"><circle cx="5" cy="7" r="5"/><circle cx="17" cy="7" r="5"/><circle cx="29" cy="7" r="5"/><circle cx="41" cy="7" r="5"/><circle cx="53" cy="7" r="5"/></g>
      <path d="M68 5 a14 14 0 0 1 20 0 l-2 2 a11 11 0 0 0 -16 0z M71 8 a9 9 0 0 1 14 0 l-2 2 a6 6 0 0 0 -10 0z M75 11 a4 4 0 0 1 6 0 l-3 3z" fill="#333"/>
    </svg>
    <div class="time">9:41 AM</div>
    <div class="battery-level">100%</div>
    <svg class="battery" width="54" height="18" viewBox="0 0 54 18" aria-hidden="true">
      <rect x="0.75" y="0.75" width="47" height="16.5" rx="3" fill="none" stroke="#333" stroke-width="1.5"/>
      <rect x="3" y="3" width="42.5" height="12" rx="1.5" fill="#333"/>
      <rect x="49.5" y="6" width="3" height="6" rx="1" fill="#333"/>
    </svg>
  </header>

  <section class="stats">
    <div class="stat lives"><div class="label">Lives</div><div class="value">3</div><div class="sub">Level N5</div></div>
    <div class="stat score"><div class="label">Score</div><div class="value">0</div><div class="sub">Highscore:8</div></div>
    <div class="stat coins"><div class="label">Coins</div><div class="value">12</div><div class="sub">Coins</div></div>
  </section>

  <div class="rule top"></div>
  <h1 class="prompt">ハク, ビャク</h1>
  <div class="rule bottom"></div>

  <main class="choices">
    <div class="choice eliminated">国</div>
    <div class="choice eliminated">石</div>
    <div class="choice">年</div>
    <div class="choice">七</div>
    <div class="choice eliminated">外</div>
    <div class="choice eliminated">毎</div>
    <div class="choice">一</div>
    <div class="choice">白</div>
    <div class="choice eliminated">新</div>
  </main>

  <nav>
    <div class="back" aria-label="Back">
      <svg width="20" height="28" viewBox="0 0 20 28" aria-hidden="true">
        <path d="M14 4 L5 14 L14 24" fill="none" stroke="#3a3a48" stroke-width="4" stroke-linecap="round" stroke-linejoin="round"/>
      </svg>
    </div>
    <div class="action level-up">Level<br>up</div>
    <div class="action live-plus">Live+<span class="cost">-24</span></div>
    <div class="action split">Split<span class="cost">-8</span></div>
    <div class="action hint">Hint<span class="cost">-4</span></div>
  </nav>
</body>
</html>
```